Bref créative
Talbert Commercial Real Estate Stationary
Business Cards, Letterhead, Fax Cover, Envelopes, Thank You Cards/Envelopes, Header & Footer
Professional
Paul Everett Talbert, Jr.
Vice President
20483 Wexmoor Road, Suite 240
Little Rock, Arkansas 72399
PETalbert@talbertcommercial-example.com
www.talbertcommercial-example.com
We would also like a powerpoint presentation if you could include that in your designs.
Thanks for all your help and God bless!
Put the Talbert Commercial logo on the back of the card or just the "R" part of the logo. We also want the following listed for our services:
Brokerage, Construction, Development, Leasing, Management
Talbert Commercial Logo Design

```html
<!DOCTYPE html>
<html lang="en">
<head>
<meta charset="utf-8">
<title>Talbert Commercial Stationery</title>
<link href="https://fonts.googleapis.com/css2?family=Montserrat:wght@400;600;800&display=swap" rel="stylesheet">
<style>
:root{
  --bg:#e6d9c5;
  --paper:#ffffff;
  --red:#c8202f;
  --charcoal:#3a3a3c;
  --grey:#8a8a8d;
  --faint:#f3e1e3;
  --shadow:rgba(0,0,0,.18);
}
*{margin:0;padding:0;box-sizing:border-box}
html,body{width:1200px;height:382px;overflow:hidden;background:var(--bg)}
body{position:relative;font-family:"Montserrat",sans-serif;color:var(--charcoal)}
.piece{position:absolute;background:var(--paper);box-shadow:0 2px 5px var(--shadow);overflow:hidden}
.brand{display:flex;align-items:center;gap:5px}
.brand-square{background:var(--red);flex:none}
.brand-name{color:var(--red);font-weight:800;line-height:1.05;text-transform:uppercase}
.caption{position:absolute;font-size:5px;color:#6b5e4d;white-space:nowrap}

/* identity block */
.identity{position:absolute;left:34px;top:30px}
.identity .brand-square{width:34px;height:34px}
.identity .brand-name{font-size:20px}
.identity .tagline{font-size:7px;color:var(--grey);margin:6px 0 0 40px}

/* business cards */
.card{width:76px;height:42px}
.card-back{left:20px}
.card-front{left:102px}
.card.row-1{top:140px}
.card.row-2{top:224px}
.card-back .brand{position:absolute;left:8px;top:9px}
.card-back .brand-square{width:9px;height:9px}
.card-back .brand-name{font-size:6px}
.card-back .services{position:absolute;left:8px;right:6px;bottom:6px;font-size:3px;color:var(--grey)}
.card-back.red{background:var(--red)}
.card-back.red .brand-square{background:#fff}
.card-back.red .brand-name,.card-back.red .services{color:#fff}
.card-front .brand{position:absolute;left:5px;top:5px}
.card-front .brand-square{width:6px;height:6px}
.card-front .brand-name{font-size:4px}
.card-front .details{position:absolute;left:5px;top:16px;font-size:2.6px;line-height:1.35}
.card-front .details strong{font-size:3.4px;display:block}
.card-front .strip{position:absolute;left:0;right:0;bottom:0;height:3px;background:var(--red)}

/* letterheads */
.letterhead{top:30px;width:212px;height:290px}
.letterhead.one{left:412px}
.letterhead.two{left:640px}
.letterhead .brand{position:absolute;left:12px;top:12px}
.letterhead .brand-square{width:12px;height:12px}
.letterhead .brand-name{font-size:7px}
.letterhead .contact{position:absolute;left:112px;top:12px;font-size:3.4px;line-height:1.5;color:var(--grey)}
.letterhead .watermark{position:absolute;left:56px;top:96px;width:100px;height:100px;background:var(--faint)}
.letterhead .foot-band{position:absolute;left:0;right:0;bottom:14px;height:4px;background:var(--red)}
.letterhead .foot-text{position:absolute;left:0;right:0;bottom:5px;text-align:center;font-size:3.4px;color:var(--grey)}

/* envelopes */
.envelope{left:1044px;width:136px;height:50px}
.envelope svg{position:absolute;inset:0}
.envelope.red-flap{top:28px}
.envelope.dark-flap{top:88px}
.envelope.plain{top:148px}
.envelope-front{left:870px;top:232px;width:312px;height:106px}
.envelope-front .brand{position:absolute;left:14px;top:12px}
.envelope-front .brand-square{width:12px;height:12px}
.envelope-front .brand-name{font-size:7px}
.envelope-front .return{position:absolute;left:14px;top:32px;font-size:3.6px;line-height:1.5;color:var(--grey)}
.envelope-front .foot-band{position:absolute;left:0;right:0;bottom:0;height:12px;background:var(--red)}
</style>
</head>
<body>

<section class="identity">
  <div class="brand"><span class="brand-square"></span><span class="brand-name">Talbert<br>Commercial</span></div>
  <p class="tagline">Stationery Concept</p>
</section>

<div class="piece card card-back row-1">
  <div class="brand"><span class="brand-square"></span><span class="brand-name">Talbert<br>Commercial</span></div>
  <p class="services">Brokerage · Construction · Development · Leasing · Management</p>
</div>
<div class="piece card card-front row-1">
  <div class="brand"><span class="brand-square"></span><span class="brand-name">Talbert Commercial</span></div>
  <p class="details"><strong>Paul Everett Talbert, Jr.</strong>Vice President<br>20483 Wexmoor Road, Suite 240<br>Little Rock, Arkansas 72399<br>PETalbert@talbertcommercial-example.com</p>
  <span class="strip"></span>
</div>
<p class="caption" style="left:20px;top:186px">Business Card Back</p>
<p class="caption" style="left:102px;top:186px">Business Card Front</p>

<div class="piece card card-back red row-2">
  <div class="brand"><span class="brand-square"></span><span class="brand-name">Talbert<br>Commercial</span></div>
  <p class="services">Brokerage · Construction · Development · Leasing · Management</p>
</div>
<div class="piece card card-front row-2">
  <div class="brand"><span class="brand-square"></span><span class="brand-name">Talbert Commercial</span></div>
  <p class="details"><strong>Paul Everett Talbert, Jr.</strong>Vice President<br>20483 Wexmoor Road, Suite 240<br>Little Rock, Arkansas 72399<br>www.talbertcommercial-example.com</p>
  <span class="strip"></span>
</div>
<p class="caption" style="left:20px;top:270px">Business Card Back</p>
<p class="caption" style="left:102px;top:270px">Business Card Front</p>

<div class="piece letterhead one">
  <div class="brand"><span class="brand-square"></span><span class="brand-name">Talbert<br>Commercial</span></div>
  <p class="contact">20483 Wexmoor Road, Suite 240<br>Little Rock, Arkansas 72399<br>Phone 501.555.0142<br>Fax 501.555.0143</p>
  <span class="watermark"></span>
  <span class="foot-band"></span>
  <p class="foot-text">www.talbertcommercial-example.com</p>
</div>
<p class="caption" style="left:496px;top:326px">Letterhead Page One</p>

<div class="piece letterhead two">
  <div class="brand"><span class="brand-square"></span><span class="brand-name">Talbert<br>Commercial</span></div>
  <p class="contact">PETalbert@talbertcommercial-example.com<br>www.talbertcommercial-example.com</p>
  <span class="watermark"></span>
  <span class="foot-band"></span>
  <p class="foot-text">www.talbertcommercial-example.com</p>
</div>
<p class="caption" style="left:724px;top:326px">Letterhead Page Two</p>

<div class="piece envelope red-flap">
  <svg viewBox="0 0 136 50" width="136" height="50"><path d="M0 0H136L68 30Z" fill="var(--red)"/><path d="M0 50L60 24M136 50L76 24" stroke="#ddd" stroke-width=".6" fill="none"/></svg>
</div>
<div class="piece envelope dark-flap">
  <svg viewBox="0 0 136 50" width="136" height="50"><path d="M0 0H136L68 30Z" fill="var(--charcoal)"/><path d="M0 50L60 24M136 50L76 24" stroke="#ddd" stroke-width=".6" fill="none"/></svg>
</div>
<div class="piece envelope plain">
  <svg viewBox="0 0 136 50" width="136" height="50"><path d="M0 0L68 30L136 0" stroke="#ccc" stroke-width=".6" fill="none"/><path d="M0 50L60 24M136 50L76 24" stroke="#ddd" stroke-width=".6" fill="none"/></svg>
</div>
<p class="caption" style="left:1096px;top:204px">Envelope Set</p>

<div class="piece envelope-front">
  <div class="brand"><span class="brand-square"></span><span class="brand-name">Talbert Commercial</span></div>
  <p class="return">20483 Wexmoor Road, Suite 240<br>Little Rock, Arkansas 72399</p>
  <span class="foot-band"></span>
</div>

</body>
</html>
```